Ecommerce Website For Printing Company

Zoravquill.com are a print, design and signage company who sell flyers, business cards, posters, brochures and more to customers in the UK.

Our website is outdated and requires a new design using current web styling and mobile functionality.

We require the following pages to be designed;
- Home Page
- Price Page
- Portfolio Page
- Blog
- Content Page

Our competitors in the printing industry are www.brenticade.com, www.hallowmarsh.co.uk, quorelvane.co.uk, www.tambridok.co.uk

We require the website to give a professional image as well as be easy for customers to navigate, understand and find prices.

Target Market(s)

Businesses

Industry/Entity Type

Printing

Number of Pages Required

4 page

Font styles to use
Sans Serif

Colors
33a6d7

Requirements
Must have
• Popular products, latest news/blog, sales from portfolio, newsletter sign up, footer

```html
<!DOCTYPE html>
<html lang="en">
<head>
<meta charset="utf-8">
<title>Zoravquill.com – Print, Design &amp; Signage</title>
<link href="https://fonts.googleapis.com/css2?family=Open+Sans:wght@400;600;700&display=swap" rel="stylesheet">
<style>
:root{
  --blue:#33a6d7;
  --blue-dark:#1f7fab;
  --ink:#333333;
  --muted:#7a7a7a;
  --topbar:#2b2b2b;
  --panel:#3a3a3a;
  --light:#eeeeee;
  --line:#dddddd;
  --green:#8cc63f;
  --white:#ffffff;
}
*{box-sizing:border-box;margin:0;padding:0}
html,body{width:713px;height:1200px;overflow:hidden}
body{font-family:"Open Sans",Arial,sans-serif;color:var(--ink);background:var(--white);font-size:10px;position:relative}
.wrap{position:absolute;left:40px;width:630px}

.topbar{position:absolute;top:0;left:0;width:713px;height:24px;background:var(--topbar);color:#cfcfcf;font-size:7px}
.topbar .wrap{height:24px;display:flex;align-items:center;justify-content:space-between}
.topbar .links{display:flex;gap:22px;align-items:center}
.topbar .basket{background:#1d1d1d;padding:6px 10px;color:var(--white);font-weight:600}

.header{position:absolute;top:24px;left:0;width:713px;height:70px;border-bottom:3px solid var(--blue)}
.logo{position:absolute;left:40px;top:14px;display:flex;align-items:center;gap:8px;font-size:24px;font-weight:700;color:var(--blue)}
.logo i{display:block;width:12px;height:12px;background:var(--blue)}
.phone{position:absolute;right:43px;top:14px;font-size:15px;color:var(--blue);font-weight:600}
.nav{position:absolute;right:43px;top:46px;display:flex;gap:16px;font-size:8px}
.nav a{color:var(--ink);text-decoration:none;padding-bottom:6px}
.nav a.active{color:var(--blue);border-bottom:2px solid var(--blue);font-weight:600}

.hero{top:102px;height:204px;display:flex;gap:12px}
.slider{position:relative;width:495px;border:1px solid var(--line);background:var(--white);padding:12px}
.slide-badge{position:absolute;left:30px;top:24px;width:120px;height:120px;border-radius:50%;background:var(--green);color:var(--white);display:flex;flex-direction:column;justify-content:center;align-items:center;text-align:center}
.slide-badge small{font-size:12px}
.slide-badge strong{font-size:22px;line-height:1.05}
.slide-photo{position:absolute;left:170px;top:18px;width:300px;height:150px;background:linear-gradient(135deg,#dfe7ee,#6fa8c9 55%,#2e4f69)}
.dots{position:absolute;bottom:10px;left:0;width:100%;display:flex;justify-content:center;gap:5px}
.dots span{width:6px;height:6px;border-radius:50%;background:#cccccc}
.dots span.on{background:var(--blue)}
.design-team{width:123px;background:var(--blue);color:var(--white);padding:12px 10px;position:relative}
.design-team h3{font-size:14px;font-weight:600;line-height:1.15}
.design-team p{font-size:6.5px;margin-top:6px;line-height:1.4}
.design-team .photo{position:absolute;left:0;bottom:0;width:100%;height:95px;background:linear-gradient(180deg,var(--blue),#1b5f80)}

.reviews{top:316px;height:45px;display:flex}
.rating{width:190px;background:var(--panel);color:var(--white);display:flex;align-items:center;gap:8px;padding:0 10px}
.rating .seal{width:26px;height:26px;border-radius:50%;background:#e0a526}
.rating p{font-size:7px;line-height:1.3}
.stars{color:#e0a526;font-size:12px;letter-spacing:1px}
.quote{flex:1;background:var(--light);padding:7px 14px;font-size:6.5px;color:var(--muted);line-height:1.45}
.quote b{display:block;color:var(--ink);font-weight:600;margin-top:2px}

.section-head{height:28px;background:var(--light);display:flex;align-items:center;justify-content:space-between;padding:0 8px}
.section-head h2{font-size:10px;color:var(--blue);font-weight:600;text-transform:uppercase}
.arrows{display:flex;gap:3px}
.arrows span{width:14px;height:14px;background:#bdbdbd;display:flex;align-items:center;justify-content:center}

.popular{top:396px}
.products{display:flex;gap:7px;margin-top:8px}
.product{width:205px}
.product .img{height:120px}
.product .label{font-size:10px;padding:7px 6px;background:var(--white);border:1px solid var(--line);border-top:0}

.blog{top:610px;height:150px;display:flex;gap:14px}
.blog .img{width:210px;height:150px;background:linear-gradient(135deg,#333,#777 60%,#aaa)}
.blog .text{flex:1}
.blog .tag{font-size:7px;color:var(--blue);font-weight:700}
.blog h3{font-size:13px;font-weight:600;margin-top:3px}
.blog .meta{font-size:6px;color:var(--muted);margin-top:2px}
.blog p{font-size:7px;color:var(--muted);line-height:1.55;margin-top:8px}

.sales{top:800px}
.portfolio{display:flex;gap:8px;margin-top:8px}
.item{width:151.5px}
.item .img{height:140px;border:1px solid var(--line)}
.item .label{font-size:7.5px;padding:6px 4px}

.newsletter{position:absolute;top:1036px;left:0;width:713px;height:36px;background:var(--blue);color:var(--white)}
.newsletter .wrap{height:36px;display:flex;align-items:center;gap:10px;font-size:7px}
.newsletter h2{font-size:12px;font-weight:600;margin-right:6px}
.newsletter .field{width:120px;height:16px;background:var(--white);color:#999;padding:3px 5px}
.check{display:flex;align-items:center;gap:4px;margin-left:8px}
.check i{width:9px;height:9px;background:var(--white);display:block}
.signup{margin-left:auto;width:80px;height:18px;background:var(--green);color:var(--white);font-weight:700;display:flex;align-items:center;justify-content:center}

.footer{position:absolute;top:1072px;left:0;width:713px;height:128px;background:#f5f5f5;text-align:center;font-size:6.5px;color:var(--muted)}
.footer .row{display:flex;justify-content:center;gap:12px;margin-top:10px}
.footer .copy{margin-top:10px;font-size:6px}
.social{display:flex;justify-content:center;gap:6px;margin-top:12px}
.social span{width:16px;height:16px;border-radius:50%;background:#555}
</style>
</head>
<body>

<div class="topbar">
  <div class="wrap">
    <span>FREE SHIPPING ON ALL ORDERS</span>
    <div class="links">
      <span>Live chat</span><span>Support</span><span>Newsletter</span><span>Your account</span>
      <span class="basket">BASKET £0.00 (0)</span>
    </div>
  </div>
</div>

<header class="header">
  <div class="logo"><i></i>Zoravquill.com</div>
  <div class="phone">Call us : 01632 960 418</div>
  <nav class="nav">
    <a class="active">Home</a><a>About</a><a>Printing</a><a>Graphic design</a><a>Website design</a><a>Artwork guide</a>
  </nav>
</header>

<section class="wrap hero">
  <div class="slider">
    <div class="slide-badge"><small>10% off</small><strong>Flyers<br>Design</strong></div>
    <div class="slide-photo" role="img" aria-label="Stack of printed flyer designs fanned out"></div>
    <div class="dots"><span class="on"></span><span></span><span></span></div>
  </div>
  <div class="design-team">
    <h3>Inhouse<br>Design Team</h3>
    <p>Professional artwork from a friendly studio team, with free proofs on every order.</p>
    <div class="photo" role="img" aria-label="Designer working at a desk in the studio"></div>
  </div>
</section>

<section class="wrap reviews">
  <div class="rating">
    <span class="seal"></span>
    <p>Our Customers<br>highly rate us</p>
    <span class="stars">★★★★☆</span>
  </div>
  <div class="quote">
    “Quick turnaround and crisp print quality every time. The team helped us fix our artwork and the flyers arrived two days early.”
    <b>Dana Morrow</b>
  </div>
</section>

<section class="wrap popular">
  <div class="section-head">
    <h2>Popular Products</h2>
    <div class="arrows"><span><svg width="6" height="8"><path d="M5 0L1 4l4 4" stroke="#fff" fill="none"/></svg></span><span><svg width="6" height="8"><path d="M1 0l4 4-4 4" stroke="#fff" fill="none"/></svg></span></div>
  </div>
  <div class="products">
    <div class="product"><div class="img" role="img" aria-label="Assorted printed business cards" style="background:linear-gradient(135deg,#7fb3d5,#c9d6e0 50%,#8d6e9c)"></div><div class="label">Business Cards</div></div>
    <div class="product"><div class="img" role="img" aria-label="Printed company letterheads" style="background:linear-gradient(135deg,#2d5f86,#dfe6ec 55%,#f2f2f2)"></div><div class="label">Letterheads</div></div>
    <div class="product"><div class="img" role="img" aria-label="Colourful printed flyers" style="background:linear-gradient(135deg,#d8cfc6,#e9a7a0 50%,#b7d3e6)"></div><div class="label">Flyers</div></div>
  </div>
</section>

<section class="wrap blog">
  <div class="img" role="img" aria-label="Digital wallpaper printed on a large office wall"></div>
  <div class="text">
    <div class="tag">BLOG</div>
    <h3>Digital Wallpaper Now Offered</h3>
    <div class="meta">Posted by Admin on 12 March 2015</div>
    <p>We now offer digital wallpaper printed on our wide format press. Choose any photo or pattern and we will print it to fit your wall, ready to hang with standard paste. It suits offices, shops and restaurants looking for a bold new look. Send us your wall size and we will prepare a free proof before printing.</p>
  </div>
</section>

<section class="wrap sales">
  <div class="section-head">
    <h2>Sales From Portfolio</h2>
    <div class="arrows"><span><svg width="6" height="8"><path d="M5 0L1 4l4 4" stroke="#fff" fill="none"/></svg></span><span><svg width="6" height="8"><path d="M1 0l4 4-4 4" stroke="#fff" fill="none"/></svg></span></div>
  </div>
  <div class="portfolio">
    <div class="item"><div class="img" role="img" aria-label="Business card design sample" style="background:linear-gradient(135deg,#ffffff,#f1e27a 60%,#c9b23a)"></div><div class="label">Business Cards</div></div>
    <div class="item"><div class="img" role="img" aria-label="Business stationery set" style="background:linear-gradient(135deg,#ffffff,#bcd7ea 60%,#3b78a8)"></div><div class="label">Business Stationery</div></div>
    <div class="item"><div class="img" role="img" aria-label="Event flyer design for a comedy night" style="background:linear-gradient(135deg,#b32025,#e9c9a0 55%,#2a2a2a)"></div><div class="label">Flyer Printing and Leaflet</div></div>
    <div class="item"><div class="img" role="img" aria-label="Event flyer design for a jazz evening" style="background:linear-gradient(135deg,#fbe7e1,#e46a5a 55%,#c2262e)"></div><div class="label">Flyer Printing and Leaflet</div></div>
  </div>
</section>

<section class="newsletter">
  <div class="wrap">
    <h2>OUR NEWSLETTER</h2>
    <div class="field">Enter your Email ID</div>
    <div class="check"><i></i>Offers</div>
    <div class="check"><i></i>Printing News</div>
    <div class="check"><i></i>All</div>
    <div class="signup">SIGN UP</div>
  </div>
</section>

<footer class="footer">
  <div class="row"><span>About</span><span>Printing</span><span>Graphic Design</span><span>Web Design</span><span>Artwork guide</span><span>Promotions</span><span>Sitemap</span><span>Contact</span><span>Downloads</span><span>Blog</span><span>Contact us</span></div>
  <div class="row" style="margin-top:6px"><span>Special Offers</span><span>Terms and Conditions</span><span>Privacy Policy</span><span>Trade account</span></div>
  <div class="copy">© 2015 Zoravquill.com. All rights reserved. Print, design and signage for UK businesses.</div>
  <div class="social"><span></span><span></span><span></span><span></span><span></span></div>
</footer>

</body>
</html>
```